LITTLE DESIGN WORK REQUIRED!

UPDATE: WE WEREN'T OVERLY ECSTATIC WITH THE DESIGNS WE WERE RECEIVING SO WE DID MOST OF THE DESIGN WORK OURSELVES...

PLEASE SEE THE NEWLY ATTACHED PPT DOC TO VIEW NEARLY EXACT REPLICAS OF WHAT WE WANT THE SITE TO LOOK LIKE. WE NOW NEED YOUR HELP TO MAKE IT LOOK LIKE SOMETHING WORTHY OF THE WEB.

NO CODING REQUIRED - EXPECTED OUTPUT PSD FILES

Hi everyone!

We're looking for a designer to work their magic for our site! We're a not-for-profit program aimed at helping young people realise their potential!

In the attached PPT file, you'll notice we've already DESIGNED THE ENTIRE SITE IN POWERPOINT. Now, we need YOU to make the small changes we requested in the document as well as design the whole thing in psd.

Any questions, don't hesitate to ask.

Brook-Rise
Updates

We've done about 95% of the design for you. Please fine-tune it. See the newly attached PPT doc for details. 

The best two designs will win. This project closes on Friday - please message us if you are absolutely sure you cannot make the deadline.

Thanks,
Brook-Rise

```html
<!DOCTYPE html>
<html lang="en">
<head>
<meta charset="utf-8">
<title>Brook-Rise</title>
<link href="https://fonts.googleapis.com/css2?family=Arimo:wght@400;700&family=Oswald:wght@500;600&family=Play:wght@400;700&display=swap" rel="stylesheet">
<style>
:root{
  --green:#7cc01e;
  --green-dark:#5f9c0c;
  --green-light:#a6dc4a;
  --ink:#1d1d1d;
  --text:#444;
  --muted:#888;
  --page:#e6e6e6;
  --panel:#f7f7f7;
  --white:#fff;
  --social:#5d77ad;
}
*{margin:0;padding:0;box-sizing:border-box}
html,body{width:960px;height:1200px;overflow:hidden}
body{background:var(--page);font-family:"Arimo",Arial,sans-serif;color:var(--text);position:relative}
.abs{position:absolute}
.topbar{left:0;top:0;width:960px;height:18px;background:var(--ink)}
.social{left:718px;top:0;width:160px;height:37px;background:var(--ink);display:flex;gap:5px;padding:4px 8px}
.social span{width:34px;height:29px;background:var(--green);display:block}
.share{left:836px;top:46px;width:45px;height:13px;background:var(--social);color:#fff;font-size:6px;line-height:13px;text-align:center;letter-spacing:.5px}
.brand{left:83px;top:56px;display:flex;align-items:center;gap:10px}
.brand i{width:30px;height:30px;border-radius:50%;background:var(--green);display:block}
.brand b{font-family:"Play",sans-serif;font-weight:700;font-size:36px;color:var(--ink);letter-spacing:-1px}
.motto{right:83px;top:62px;text-align:right;font-family:"Play",sans-serif;font-weight:700;font-size:14px;line-height:17px;color:#666}
.motto em{font-style:normal;color:var(--green)}
.enquiry{right:83px;top:118px;font-family:"Oswald",sans-serif;font-weight:600;font-size:20px;color:#555;display:flex;align-items:center;gap:6px}
.enquiry span{color:var(--green)}
.enquiry svg{width:20px;height:20px}
.panel{left:80px;top:150px;width:800px;height:1060px;background:var(--panel)}
.nav{left:80px;top:150px;width:800px;height:36px;display:flex;align-items:center}
.nav a{font-family:"Play",sans-serif;font-weight:700;font-size:12px;color:#555;text-decoration:none;letter-spacing:.5px;position:absolute;transform:translateX(-50%);top:8px}
.nav .sep{position:absolute;top:8px;width:1px;height:22px;background:#ddd}
.home{left:107px;top:140px;width:82px;height:46px;background:linear-gradient(var(--green-light),var(--green));color:#fff;font-family:"Play",sans-serif;font-weight:700;font-size:12px;text-align:center;line-height:46px;letter-spacing:.5px}
.searchtab{left:593px;top:198px;width:267px;height:40px;background:var(--ink);border-radius:14px 14px 0 0}
.search{left:638px;top:207px;width:197px;height:25px;background:#fff;border-radius:3px;font-size:9px;color:#888;padding:7px 14px}
.search svg{position:absolute;right:4px;top:3px}
.hero{left:82px;top:233px;width:796px;height:313px;border:5px solid var(--green);background:#fff}
.hero-img{left:87px;top:238px;width:533px;height:303px;background:radial-gradient(circle at 30% 45%,#e8d5c4,#f2f2f2 45%,#eaeaea 80%)}
.feats{left:620px;top:233px;width:240px;height:287px;background:linear-gradient(#111,#2a2a2a);color:#fff;padding:16px 18px}
.feats h2{font-family:"Play",sans-serif;font-weight:700;font-size:30px;color:var(--green);line-height:34px}
.feats h3{font-family:"Play",sans-serif;font-weight:700;font-size:14px;line-height:17px;margin-top:8px}
.feats p{font-size:9.5px;line-height:16px;margin-top:12px;text-align:justify;letter-spacing:.3px}
.arrow{left:734px;top:520px;width:0;height:0;border-left:6px solid transparent;border-right:6px solid transparent;border-top:7px solid #2a2a2a}
.more{left:680px;top:454px;width:122px;height:28px;background:var(--green);clip-path:polygon(8% 0,92% 0,100% 50%,92% 100%,8% 100%,0 50%);color:#fff;font-family:"Play",sans-serif;font-weight:700;font-size:12px;text-align:center;line-height:28px}
.more span{color:var(--green-light)}
.h-green{font-family:"Play",sans-serif;font-weight:700;color:#555}
.h-green em{font-style:normal;color:var(--green)}
.welcome{left:93px;top:570px;font-size:19px}
.intro{left:93px;top:601px;width:545px;font-size:9.5px;line-height:16px;letter-spacing:.3px;color:#777}
.intro p+p{margin-top:16px}
.intro b{color:#555}
.readmore{left:569px;top:699px;font-size:9.5px;color:var(--green);font-weight:700}
.rule{left:93px;top:724px;width:545px;height:1px;background:#ddd}
.recent{left:96px;top:736px;display:flex;align-items:center;gap:10px;font-size:16px}
.recent i{width:34px;height:34px;border-radius:50%;background:var(--green-light);display:block}
.banner{left:89px;top:785px;width:508px;height:22px;border-radius:6px;background:linear-gradient(var(--green-light),var(--green));color:#fff;font-family:"Play",sans-serif;font-weight:700;font-size:13px;line-height:22px;padding-left:10px}
.card{width:233px;height:159px;background:#fff;border:1px solid #e2e2e2;padding:6px 7px}
.card div{width:100%;height:100%}
.pic-campus{background:linear-gradient(#9bb0c8 0%,#9a8a70 40%,#6f8f3c 62%,#5a7b2c 100%)}
.pic-group{background:linear-gradient(90deg,#d8c7b2,#f0f0f0 50%,#c9b6a0)}
.pic-study{background:linear-gradient(#6ea03a,#b99d7c 60%,#5c7d2e)}
.post h4{font-family:"Play",sans-serif;font-weight:700;font-size:13px;color:var(--green-dark);letter-spacing:.5px}
.post p{font-size:9.5px;line-height:14.5px;margin-top:6px;width:218px;letter-spacing:.5px;color:#444}
.fb{left:666px;top:582px;width:210px;height:238px;background:#fff;border:1px solid #c8d0e0}
.fb-head{height:26px;background:var(--social);color:#fff;display:flex;justify-content:space-between;align-items:center;padding:0 6px}
.fb-head b{font-family:"Arimo",sans-serif;font-size:15px}
.fb-head span{font-size:8.5px}
.fb-page{display:flex;gap:8px;padding:10px 6px 8px;border-bottom:1px solid #eee}
.fb-page i{width:58px;height:28px;background:#eee;display:block}
.fb-page b{font-family:"Play",sans-serif;font-size:10px;color:var(--social);display:block}
.fb-page small{font-size:8px;color:#777}
.fb-page small span{border:1px solid #ccd;padding:0 3px;margin-right:4px;color:var(--social)}
.fb-item{display:flex;gap:8px;padding:5px 10px 4px}
.fb-item i{width:24px;height:24px;background:#b7c4dc;display:block;flex:none}
.fb-item b{font-family:"Play",sans-serif;font-size:8.5px;color:var(--social);display:block;letter-spacing:.3px}
.fb-item small{font-size:7.5px;color:#999}
.fb-foot{position:absolute;left:8px;bottom:4px;font-size:7px;color:#555;display:flex;gap:4px;align-items:center;border-top:1px solid #ddd;width:192px;padding-top:4px}
.fb-foot i{width:10px;height:10px;background:var(--social);display:block}
.popular{left:674px;top:850px;font-size:19px}
.pop{left:676px;width:194px}
.pop h5{font-family:"Play",sans-serif;font-weight:700;font-size:10.5px;color:var(--green-dark);letter-spacing:.3px;position:relative}
.pop h5::before{content:"";position:absolute;left:-8px;top:3px;border-left:4px solid var(--green);border-top:3.5px solid transparent;border-bottom:3.5px solid transparent}
.pop p{font-size:8.5px;line-height:13px;color:#555;text-align:justify;margin-top:1px}
.pop a{display:block;text-align:right;font-size:8px;font-style:italic;color:var(--green-dark);text-decoration:underline;margin-top:3px}
.rule2{left:672px;top:1102px;width:186px;height:1px;background:#ddd}
.know{left:670px;top:1111px;font-size:19px}
.avatar{left:668px;top:1146px;width:40px;height:40px;background:linear-gradient(#f4f4f4,#dcdcdc);border:1px solid #ddd}
.john{left:722px;top:1145px;width:140px}
.john b{font-family:"Play",sans-serif;font-size:10.5px;color:var(--green-dark)}
.john p{font-size:8.5px;line-height:12px;color:#555}
.john a{display:block;text-align:right;font-size:8px;font-style:italic;color:var(--green-dark);text-decoration:underline;margin-right:18px}
</style>
</head>
<body>
<div class="abs topbar"></div>
<div class="abs social" aria-label="Social links"><span></span><span></span><span></span><span></span></div>
<div class="abs share">SHARE</div>

<div class="abs brand"><i></i><b>BROOK RISE</b></div>
<div class="abs motto"><em>“ What would you do if you</em><br>knew you could not fail? ”</div>
<div class="abs enquiry">
  <svg viewBox="0 0 20 20"><path d="M4 2h4l2 5-3 2a11 11 0 0 0 4 4l2-3 5 2v4a2 2 0 0 1-2 2A16 16 0 0 1 2 4a2 2 0 0 1 2-2z" fill="#7cc01e"/></svg>
  <span>Enquiries:</span> +61 (3) 5550 1842
</div>

<div class="abs panel"></div>
<nav class="abs nav">
  <a style="left:178px">About Us</a>
  <span class="sep" style="left:127px"></span>
  <a style="left:286px">Resources</a>
  <span class="sep" style="left:232px"></span>
  <a style="left:391px">Article</a>
  <span class="sep" style="left:345px"></span>
  <a style="left:511px">Work-shops</a>
  <span class="sep" style="left:442px"></span>
  <a style="left:642px">Ambassadors</a>
  <span class="sep" style="left:576px"></span>
  <a style="left:750px">Feats</a>
  <span class="sep" style="left:709px"></span>
</nav>
<div class="abs home">Home</div>

<div class="abs searchtab"></div>
<div class="abs search">Enter Keyword
  <svg width="20" height="19" viewBox="0 0 20 19"><circle cx="12" cy="7" r="5" fill="none" stroke="#999" stroke-width="1.6"/><path d="M8 11l-5 5" stroke="#999" stroke-width="2"/></svg>
</div>

<div class="abs hero"></div>
<div class="abs hero-img" role="img" aria-label="Smiling young people with folders and books standing together"></div>
<section class="abs feats">
  <h2>FEATS</h2>
  <h3>Challenges that dare you to push yourself.</h3>
  <p>Lorem Ipsum is simply dummy text of the printing and typesetting industry. Lorem Ipsum has been the industry's standard dummy text ever since the 1500s, when an unknown printer took a galley of type and scrambled it to make a type specimen book.make a type specimen book.</p>
</section>
<div class="abs arrow"></div>
<div class="abs more">More <span>Details</span></div>

<h1 class="abs h-green welcome"><em>Welcome to</em> Brook-Rise</h1>
<div class="abs intro">
  <p><b>Brook-Rise is a not-for-profit program aimed at helping people</b> – especially young people – realise their potential and achieve success. Brook-Rise is a not-for-profit program aimed at helping people – especially young people – realise their potential and achieve success.</p>
  <p><b>Our resources are categorised into four groups: discovery,</b> design, build, and achieve – the four steps in our achievement framework. Our resources are categorised into four groups: discovery, design, build, and achieve – the four steps in our achievement framework.</p>
</div>
<div class="abs readmore">Readmore [+]</div>
<div class="abs rule"></div>
<h2 class="abs h-green recent"><i></i><span><em>Recent</em> Posts</span></h2>
<div class="abs banner">Our resources are categorised into four groups: discovery, design.</div>

<div class="abs card" style="left:98px;top:824px"><div class="pic-campus" role="img" aria-label="Students studying on a campus lawn"></div></div>
<div class="abs card" style="left:367px;top:824px"><div class="pic-group" role="img" aria-label="Row of smiling students holding notebooks"></div></div>
<article class="abs post" style="left:102px;top:992px"><h4>Lorem ipsum dolor</h4><p>Our resources are categorised into four groups: <b>discovery</b>, <b>design</b>, build, and achieve the four steps in our achievement</p></article>
<article class="abs post" style="left:371px;top:992px"><h4>Lorem ipsum dolor</h4><p>Our resources are categorised into four groups: <b>discovery</b>, <b>design</b>, build, and achieve the four steps in our achievement</p></article>
<div class="abs card" style="left:98px;top:1080px;height:140px"><div class="pic-study" role="img" aria-label="Students reading together outdoors"></div></div>
<div class="abs card" style="left:367px;top:1080px;height:140px"><div class="pic-campus" role="img" aria-label="Students studying on a campus lawn"></div></div>

<aside class="abs fb">
  <div class="fb-head"><b>Circlewall</b><span>Find us on Circlewall</span></div>
  <div class="fb-page"><i></i><div><b>Brook Rise</b><small><span>Like</span>3,564 people like this.</small></div></div>
  <div class="fb-item"><i></i><div><b>Eat plain popcorn when you are</b><small>3,564 people Shared this.</small></div></div>
  <div class="fb-item"><i></i><div><b>Eat plain popcorn when you are</b><small>3,564 people Shared this.</small></div></div>
  <div class="fb-item"><i></i><div><b>Eat plain popcorn when you are</b><small>3,564 people Shared this.</small></div></div>
  <div class="fb-item"><i></i><div><b>Eat plain popcorn when you are</b><small>3,564 people Shared this.</small></div></div>
  <div class="fb-foot"><i></i>Circlewall social plugin</div>
</aside>

<h2 class="abs h-green popular"><em>Popular</em> Posts</h2>
<div class="abs pop" style="top:882px"><h5>Lorem ipsum dolor</h5><p>Lorem ipsum dolor sit amet, Lorem ipsum dolor sit amet, consecteturLorem ipsum dolor sit amet, consectetur</p><a>587 views (s)</a></div>
<div class="abs pop" style="top:948px"><h5>Lorem ipsum dolor</h5><p>Lorem ipsum dolor sit amet, Lorem ipsum dolor sit amet, consecteturLorem ipsum dolor sit amet, consectetur</p><a>587 views (s)</a></div>
<div class="abs pop" style="top:1015px"><h5>Lorem ipsum dolor</h5><p>Lorem ipsum dolor sit amet, Lorem ipsum dolor sit amet, consecteturLorem ipsum dolor sit amet, consectetur</p><a>587 views (s)</a></div>
<div class="abs rule2"></div>
<h2 class="abs h-green know"><em>Get To</em> Know Us</h2>
<div class="abs avatar" role="img" aria-label="Team member avatar"></div>
<div class="abs john"><b>John Doe</b><p>Lorem ipsum dolor sit amet, consectetur</p><a>Meet John</a></div>
</body>
</html>
```